Business Card for Pottery and Jewellery Designer

A new business card design is needed to accompany a newly launching pottery and jewellery website. The company logo has been attached for use. The company is called Glazewick Studio. For a sense of the vibe please see the website (it is currently under construction but this way you'll get a feel for the style) www.GlazewickStudio.com

The website font is Pontano Sans for the body of the text with Overlock for headers.

The overall look should be clean and elegant. The back side can have just the logo. The front side should have a smaller logo and the following details displayed:

Glazewick Studio
Designer: Hollis Marrow
Phone: xxx.xxx.xxxx
Email: Designer@GlazewickStudio.com

The structure of displaying this is completely up to you. Different layouts and creative methods of displaying contact info are welcome as long as it stays clean/uncluttered.

No product photographs are to be included in the design as the catalogue changes quickly.

Colour preferences lean towards elegant and understated (charcoal grey, dark navy blue etc.)

Please let me know if you have any further questions or further details required.

Target Market(s)

Target market is 30+ year old women

Industry/Entity Type

Construction

Colors
ffffff
1b1b1b
474747
d9d9d9
fafafa
0355a3

Requirements
Must have
• The submissions so far have looked very typical and don't stand out right now. They're also all in navy with very little variation. I'm looking for something that stands out a it more while still being clean-looking.
Nice to have
• I've attached a few design samples and an idea for a backdrop. It would be great to see some designs in black, white, and grey with only a hint of color.
Should not have
• Product Images

```html
<!DOCTYPE html>
<html lang="en">
<head>
<meta charset="utf-8">
<title>Glazewick Studio – Business Card</title>
<link href="https://fonts.googleapis.com/css2?family=Didact+Gothic&display=swap" rel="stylesheet">
<style>
  :root {
    --paper: #ffffff;
    --backdrop: #f1f1f1;
    --charcoal: #3a3a3a;
    --ink: #1b1b1b;
    --mid-grey: #474747;
    --light-grey: #d9d9d9;
    --accent-blue: #0348a3;
    --shadow: rgba(0, 0, 0, 0.12);
  }
  * { margin: 0; padding: 0; box-sizing: border-box; }
  html, body {
    width: 1200px;
    height: 720px;
    overflow: hidden;
    background: var(--backdrop);
    font-family: "Didact Gothic", "Century Gothic", sans-serif;
  }
  .canvas {
    position: relative;
    width: 1200px;
    height: 720px;
  }
  .card {
    position: absolute;
    top: 205px;
    width: 540px;
    height: 309px;
    background: var(--paper);
    box-shadow: 0 6px 18px var(--shadow);
    overflow: hidden;
  }
  .card--back { left: 40px; }
  .card--front { left: 620px; }

  /* Back side */
  .back-brand {
    position: absolute;
    inset: 0;
    display: flex;
    align-items: center;
    justify-content: center;
    gap: 16px;
  }
  .back-brand__dot {
    width: 46px;
    height: 46px;
    border-radius: 50%;
    background: var(--ink);
  }
  .back-brand__name {
    font-size: 40px;
    color: var(--ink);
    letter-spacing: 0.5px;
  }

  /* Front side */
  .front-panel {
    position: absolute;
    inset: 0;
    width: 540px;
    height: 309px;
  }
  .front-brand {
    position: absolute;
    left: 28px;
    top: 68px;
    display: flex;
    align-items: center;
    gap: 10px;
  }
  .front-brand__dot {
    width: 22px;
    height: 22px;
    border-radius: 50%;
    background: var(--ink);
  }
  .front-brand__name {
    font-size: 17px;
    color: var(--accent-blue);
  }
  .contact {
    position: absolute;
    right: 40px;
    top: 72px;
    text-align: right;
    color: var(--light-grey);
  }
  .contact__name {
    font-size: 22px;
    color: var(--accent-blue);
    line-height: 1.1;
  }
  .contact__role {
    font-size: 15px;
    color: #f2f2f2;
    margin-top: 2px;
  }
  .contact__list {
    list-style: none;
    margin-top: 44px;
    margin-right: -22px;
  }
  .contact__item {
    display: flex;
    align-items: center;
    justify-content: flex-end;
    gap: 8px;
    font-size: 12px;
    line-height: 1;
    margin-bottom: 11px;
  }
  .contact__item--phone { font-size: 10px; }
  .contact__icon { width: 12px; height: 12px; flex: none; }
</style>
</head>
<body>
<main class="canvas">

  <section class="card card--back" aria-label="Card back">
    <div class="back-brand">
      <span class="back-brand__dot"></span>
      <span class="back-brand__name">Glazewick Studio</span>
    </div>
  </section>

  <section class="card card--front" aria-label="Card front">
    <svg class="front-panel" viewBox="0 0 540 309" aria-hidden="true">
      <path d="M250 0 Q232 150 262 309 L272 309 Q240 150 292 0 Z" fill="var(--accent-blue)"/>
      <path d="M292 0 Q240 150 272 309 L540 309 L540 0 Z" fill="var(--charcoal)"/>
    </svg>

    <div class="front-brand">
      <span class="front-brand__dot"></span>
      <span class="front-brand__name">Glazewick Studio</span>
    </div>

    <div class="contact">
      <p class="contact__name">Hollis Marrow</p>
      <p class="contact__role">Designer</p>
      <ul class="contact__list">
        <li class="contact__item contact__item--phone">
          <span>xxx.xxx.xxxx</span>
          <svg class="contact__icon" viewBox="0 0 12 12" aria-hidden="true">
            <rect x="3" y="0.5" width="6" height="11" rx="1.2" fill="none" stroke="var(--accent-blue)" stroke-width="1.2"/>
            <line x1="5" y1="9.5" x2="7" y2="9.5" stroke="var(--accent-blue)" stroke-width="1"/>
          </svg>
        </li>
        <li class="contact__item">
          <span>Designer@GlazewickStudio.com</span>
          <svg class="contact__icon" viewBox="0 0 12 12" aria-hidden="true">
            <rect x="0.6" y="2.5" width="10.8" height="7" fill="none" stroke="var(--accent-blue)" stroke-width="1.2"/>
            <polyline points="0.6,2.5 6,6.5 11.4,2.5" fill="none" stroke="var(--accent-blue)" stroke-width="1.2"/>
          </svg>
        </li>
      </ul>
    </div>
  </section>

</main>
</body>
</html>
```